Tallowreed Advisory Partners Business Card Design

We have the logo we just need someone to design a modern business card design.

Name: Desmond Munkalt
Phone: 3055550148
Mobile: 9175550193
Web:www.tallowreedadvisory.example
email: dmunkalt@tallowreedadvisory.example
Company: Tallowreed Advisory Partners
Title: CEO

Address: 718 Quillmore Ave, Miami, Florida 33190

Target Market(s)

companies over 100 employees

Industry/Entity Type

Business

```html
<!DOCTYPE html>
<html lang="en">
<head>
<meta charset="utf-8">
<title>Tallowreed Advisory Partners – Business Card</title>
<link href="https://fonts.googleapis.com/css2?family=Open+Sans:wght@400;600;700&display=swap" rel="stylesheet">
<style>
  :root {
    --backdrop: #dcdcdc;
    --card-dark: #3c3c3c;
    --card-white: #ffffff;
    --brand-blue: #1f6ff0;
    --band-grey: #6e6e6e;
    --ink: #2a2a2a;
    --ink-soft: #4a4a4a;
    --divider: #8a8a8a;
    --pale-text: #e6e6e6;
  }
  * { box-sizing: border-box; margin: 0; padding: 0; }
  html, body {
    width: 1200px; height: 968px; overflow: hidden;
    background: var(--backdrop);
    font-family: "Open Sans", Arial, sans-serif;
  }
  .sheet {
    width: 1200px; height: 968px;
    display: flex; flex-direction: column; align-items: center; justify-content: center;
    gap: 44px;
  }
  .card {
    position: relative;
    width: 600px; height: 343px;
    border-radius: 4px;
    overflow: hidden;
    box-shadow: 0 6px 18px rgba(0,0,0,0.18);
  }

  /* Front */
  .card-front {
    background: var(--card-dark);
    display: flex; flex-direction: column; align-items: center; justify-content: center;
    gap: 22px;
  }
  .brand-dot {
    width: 96px; height: 96px; border-radius: 50%;
    background: var(--brand-blue);
  }
  .brand-name {
    color: var(--card-white);
    font-weight: 700;
    font-size: 30px;
    letter-spacing: 2px;
    text-transform: uppercase;
    text-align: center;
    line-height: 1.2;
  }

  /* Back */
  .card-back { background: var(--card-white); }
  .card-back .bands { position: absolute; inset: 0; }
  .holder-name {
    position: absolute; left: 26px; top: 30px;
    color: var(--card-white);
    font-weight: 700; font-size: 23px;
  }
  .holder-title {
    position: absolute; left: 318px; top: 16px;
    color: var(--pale-text);
    font-weight: 400; font-size: 15px; letter-spacing: 0.5px;
  }
  .back-brand {
    position: absolute; left: 34px; top: 150px; width: 190px;
    display: flex; flex-direction: column; align-items: center; gap: 12px;
  }
  .back-brand .brand-dot { width: 54px; height: 54px; }
  .back-brand .brand-name {
    color: var(--ink); font-size: 15px; letter-spacing: 1px;
  }
  .divider {
    position: absolute; left: 242px; top: 96px;
    width: 1px; height: 186px; background: var(--divider);
  }
  .contact-list {
    position: absolute; left: 262px; top: 98px;
    list-style: none;
    display: flex; flex-direction: column; gap: 9px;
  }
  .contact-item {
    display: flex; align-items: center; gap: 12px;
    color: var(--ink-soft); font-size: 15px; line-height: 1.25;
  }
  .contact-icon {
    flex: 0 0 24px; width: 24px; height: 24px;
  }
</style>
</head>
<body>
<main class="sheet">

  <section class="card card-front" aria-label="Card front">
    <div class="brand-dot"></div>
    <p class="brand-name">Tallowreed<br>Advisory Partners</p>
  </section>

  <section class="card card-back" aria-label="Card back">
    <svg class="bands" width="600" height="343" viewBox="0 0 600 343" aria-hidden="true">
      <path d="M285 14 H600 V44 H285 Z" fill="var(--band-grey)"/>
      <path d="M0 0 H600 V14 H312 C292 14 292 74 270 74 H0 Z" fill="var(--brand-blue)"/>
      <rect x="0" y="300" width="600" height="6" fill="var(--band-grey)"/>
      <rect x="0" y="312" width="600" height="31" fill="var(--brand-blue)"/>
      <rect x="0" y="322" width="600" height="1.5" fill="var(--card-white)" opacity="0.7"/>
    </svg>

    <h1 class="holder-name">Desmond Munkalt</h1>
    <p class="holder-title">CEO</p>

    <div class="back-brand">
      <div class="brand-dot"></div>
      <p class="brand-name">Tallowreed<br>Advisory Partners</p>
    </div>

    <div class="divider"></div>

    <ul class="contact-list">
      <li class="contact-item">
        <svg class="contact-icon" viewBox="0 0 24 24" aria-label="Mobile"><circle cx="12" cy="12" r="12" fill="var(--brand-blue)"/><rect x="8.5" y="5.5" width="7" height="13" rx="1.3" fill="none" stroke="#fff" stroke-width="1.6"/><circle cx="12" cy="16" r="0.9" fill="#fff"/></svg>
        <span>9175550193</span>
      </li>
      <li class="contact-item">
        <svg class="contact-icon" viewBox="0 0 24 24" aria-label="Phone"><circle cx="12" cy="12" r="12" fill="var(--brand-blue)"/><path d="M8 6.5 L10.2 6.5 L11 9.6 L9.6 10.6 C10.4 12.3 11.7 13.6 13.4 14.4 L14.4 13 L17.5 13.8 L17.5 16 C17.5 16.8 16.8 17.5 16 17.5 C10.8 17.2 6.8 13.2 6.5 8 C6.5 7.2 7.2 6.5 8 6.5 Z" fill="#fff"/></svg>
        <span>3055550148</span>
      </li>
      <li class="contact-item">
        <svg class="contact-icon" viewBox="0 0 24 24" aria-label="Email"><circle cx="12" cy="12" r="12" fill="var(--brand-blue)"/><rect x="6" y="8" width="12" height="8.5" rx="1" fill="#fff"/><path d="M6.5 8.6 L12 12.6 L17.5 8.6" fill="none" stroke="var(--brand-blue)" stroke-width="1.3"/></svg>
        <span>dmunkalt@tallowreedadvisory.example</span>
      </li>
      <li class="contact-item">
        <svg class="contact-icon" viewBox="0 0 24 24" aria-label="Website"><circle cx="12" cy="12" r="12" fill="var(--brand-blue)"/><circle cx="12" cy="12" r="6" fill="none" stroke="#fff" stroke-width="1.4"/><ellipse cx="12" cy="12" rx="2.6" ry="6" fill="none" stroke="#fff" stroke-width="1.2"/><line x1="6" y1="12" x2="18" y2="12" stroke="#fff" stroke-width="1.2"/></svg>
        <span>www.tallowreedadvisory.example</span>
      </li>
      <li class="contact-item">
        <svg class="contact-icon" viewBox="0 0 24 24" aria-label="Address"><circle cx="12" cy="12" r="12" fill="var(--brand-blue)"/><path d="M12 5.5 C9.2 5.5 7.3 7.5 7.3 10 C7.3 13.3 12 18.5 12 18.5 C12 18.5 16.7 13.3 16.7 10 C16.7 7.5 14.8 5.5 12 5.5 Z" fill="#fff"/><circle cx="12" cy="10" r="1.8" fill="var(--brand-blue)"/></svg>
        <span>718 Quillmore Ave,<br>Miami, Florida 33190</span>
      </li>
    </ul>
  </section>

</main>
</body>
</html>
```